Business Card Design

We need a business card designed for our new company. Prefer a black card with white logo & writing.

Contact Information for Business Card

Dale Pickett, address: 7-4417 Larchmere Avenue, Abbotsford, BC, V3K 2R9, Office Phone: 604-555-0172, Cell: 604-555-0138, Email: dale@kelsoncoatworks.ca

Colors

Designer to choose only greyscale colors for use in the design.

```html
<!DOCTYPE html>
<html lang="en">
<head>
<meta charset="utf-8">
<title>Kelson Coatworks – Business Card</title>
<link href="https://fonts.googleapis.com/css2?family=Poppins:wght@300;400;700&display=swap" rel="stylesheet">
<style>
  :root {
    --backdrop: #252525;
    --card: #1c1c1d;
    --ink: #ffffff;
    --ink-soft: #e6e6e6;
    --rule: #9a9a9a;
  }
  * { box-sizing: border-box; margin: 0; padding: 0; }
  html, body {
    width: 1200px; height: 780px; overflow: hidden;
    background: var(--backdrop);
    font-family: "Poppins", sans-serif;
    color: var(--ink);
  }
  .sheet {
    width: 1200px; height: 780px;
    display: flex; align-items: center; justify-content: center; gap: 36px;
  }
  .card {
    width: 560px; height: 320px;
    background: var(--card);
    box-shadow: 0 18px 40px rgba(0,0,0,.55);
    position: relative;
    display: flex; align-items: center;
  }
  .brand {
    display: flex; align-items: center; gap: 10px;
  }
  .brand-dot {
    width: 22px; height: 22px; border-radius: 50%;
    background: var(--ink); flex: none;
  }
  .brand-name {
    font-weight: 700; text-transform: uppercase; line-height: 1.05;
    color: var(--ink);
  }
  /* front */
  .card-front .logo-side {
    width: 46%; height: 100%;
    display: flex; align-items: center; justify-content: center;
  }
  .card-front .brand-name { font-size: 24px; }
  .divider {
    width: 1px; height: 62%;
    background: linear-gradient(to bottom, transparent, var(--rule) 30%, var(--ink) 50%, var(--rule) 70%, transparent);
  }
  .contact-side {
    flex: 1; padding-left: 30px;
  }
  .person-name { font-size: 25px; line-height: 1.1; font-weight: 300; }
  .person-name strong { font-weight: 700; }
  .person-title { font-size: 12.5px; font-weight: 300; color: var(--ink-soft); margin-bottom: 12px; }
  .address { font-size: 12.5px; font-weight: 300; line-height: 1.45; color: var(--ink-soft); margin-bottom: 12px; }
  .contact-list { list-style: none; }
  .contact-list li {
    display: flex; align-items: center; gap: 9px;
    font-size: 12.5px; font-weight: 300; line-height: 1.75; color: var(--ink-soft);
  }
  .contact-list svg { width: 12px; height: 12px; flex: none; }
  /* back */
  .card-back { justify-content: center; }
  .card-back .brand-dot { width: 34px; height: 34px; }
  .card-back .brand-name { font-size: 38px; }
</style>
</head>
<body>
<main class="sheet">
  <section class="card card-front">
    <div class="logo-side">
      <div class="brand">
        <span class="brand-dot"></span>
        <span class="brand-name">Kelson<br>Coatworks</span>
      </div>
    </div>
    <div class="divider"></div>
    <div class="contact-side">
      <p class="person-name"><strong>Dale</strong> Pickett</p>
      <p class="person-title">Founder &amp; CEO</p>
      <p class="address">7-4417 Larchmere Avenue,<br>Abbotsford, BC, V3K 2R9.</p>
      <ul class="contact-list">
        <li>
          <svg viewBox="0 0 24 24" fill="#fff"><path d="M6.6 10.8a15 15 0 0 0 6.6 6.6l2.2-2.2c.3-.3.7-.4 1-.2 1.1.4 2.3.6 3.6.6.6 0 1 .4 1 1V20c0 .6-.4 1-1 1A17 17 0 0 1 3 4c0-.6.4-1 1-1h3.5c.6 0 1 .4 1 1 0 1.3.2 2.5.6 3.6.1.3 0 .7-.2 1z"/></svg>
          604-555-0172
        </li>
        <li>
          <svg viewBox="0 0 24 24" fill="none" stroke="#fff" stroke-width="2.4"><rect x="3" y="4" width="18" height="16" rx="1"/><rect x="7" y="9" width="6" height="6" fill="#fff" stroke="none"/></svg>
          604-555-0138
        </li>
        <li>
          <svg viewBox="0 0 24 24" fill="none" stroke="#fff" stroke-width="2"><circle cx="12" cy="12" r="9"/><path d="M3 12h18M12 3c3 3 3 15 0 18M12 3c-3 3-3 15 0 18"/></svg>
          www.kelsoncoatworks.ca
        </li>
        <li>
          <svg viewBox="0 0 24 24" fill="none" stroke="#fff" stroke-width="2"><rect x="3" y="6" width="18" height="13" rx="1"/><path d="M3 7l9 6 9-6"/></svg>
          dale@kelsoncoatworks.ca
        </li>
      </ul>
    </div>
  </section>

  <section class="card card-back">
    <div class="brand">
      <span class="brand-dot"></span>
      <span class="brand-name">Kelson<br>Coatworks</span>
    </div>
  </section>
</main>
</body>
</html>
```